Varnek Semi truck

Hello Designers! I represent a truck driving company in need of a design for our new company trucks & trailers (new Brenta, Dalmoor & roadmaster pellora). I want it modern, not too complicated, & eye catching. I will attach the logo, you can incorporate the symbol as part of the design. If desired, "Drive varnek" can be added to the trailer. The trucks & trailers are going to be white.
I want the back door of the trailer to have our logo or drive4varnek.com
The attached picture of the truck is grey and the logo is gold. The trucks are going to be the same but in white, so we will use the blue Varnek Logo. We are also not sure if we want anything on the cab because we don't want it to feel overwhelming. If you have any questions please ask at mirela@varnek.example. We will tip well for the design we pick. Thank you!

Target Market(s)

Drivers on the road

Industry/Entity Type

Truck driving company

Colors
0094D4
00A9DD
6FCCEA
C7EBF8
E9F6FB

Requirements
Must have
• Our website address to be included on the trailer (not in large print, medium-small): www. drivevarnek .com
Nice to have
• Some kind of pattern on the trailer, possibly cab as well.
Should not have
• any other bright colors other then the logo. A simple line is fine but nothing competing with the logo.

```html
<!DOCTYPE html>
<html lang="en">
<head>
<meta charset="utf-8">
<title>Varnek Trailer Livery</title>
<link rel="stylesheet" href="https://fonts.googleapis.com/css2?family=Jost:wght@600&family=Montserrat:wght@700&display=swap">
<style>
  :root {
    --bg: #e6e7e9;
    --panel: #ffffff;
    --panel-edge: #d4d6d9;
    --brand-dark: #1d4f63;
    --brand-mid: #3f8597;
    --brand-teal: #6fbfc4;
    --brand-pale: #bfe3e3;
    --contact: #555a5e;
  }
  html, body {
    margin: 0;
    padding: 0;
    width: 1200px;
    height: 1200px;
    overflow: hidden;
    background: var(--bg);
  }
  .canvas {
    position: relative;
    width: 1200px;
    height: 1200px;
  }
  .trailer-side {
    position: absolute;
    width: 866px;
    height: 180px;
    background: var(--panel);
    box-shadow: inset 0 0 0 1px var(--panel-edge);
  }
  .trailer-side--right { left: 164px; top: 266px; }
  .trailer-side--left  { left: 172px; top: 708px; }
  .trailer-side__pattern {
    position: absolute;
    inset: 0;
    width: 866px;
    height: 180px;
  }
  .brand-mark {
    position: absolute;
    left: 281px;
    top: 32px;
    width: 84px;
    height: 84px;
    background: var(--brand-mid);
  }
  .brand-name {
    position: absolute;
    left: 403px;
    top: 44px;
    margin: 0;
    font-family: "Jost", sans-serif;
    font-weight: 600;
    font-size: 56px;
    line-height: 1;
    color: var(--brand-dark);
  }
  .contact-phone,
  .contact-web {
    position: absolute;
    margin: 0;
    font-family: "Montserrat", sans-serif;
    font-weight: 700;
    line-height: 1;
    color: var(--contact);
  }
  .contact-phone { left: 415px; top: 115px; font-size: 17px; }
  .contact-web   { left: 372px; top: 136px; font-size: 18px; }
</style>
</head>
<body>
<div class="canvas">
  <svg width="0" height="0" style="position:absolute" aria-hidden="true">
    <defs>
      <linearGradient id="facet-tones" x1="0" y1="0" x2="1" y2="1">
        <stop offset="0" stop-color="#1d4f63"/>
        <stop offset="0.45" stop-color="#3f8597"/>
        <stop offset="0.75" stop-color="#6fbfc4"/>
        <stop offset="1" stop-color="#2d6a7d"/>
      </linearGradient>
    </defs>
  </svg>

  <section class="trailer-side trailer-side--right">
    <svg class="trailer-side__pattern" viewBox="0 0 866 180">
      <polygon role="img" aria-label="Faceted teal triangle pattern at front end" points="0,0 110,0 0,175" fill="url(#facet-tones)"/>
      <polygon role="img" aria-label="Faceted teal triangle pattern at rear end" points="836,0 866,0 866,180 742,180" fill="url(#facet-tones)"/>
    </svg>
    <div class="brand-mark"></div>
    <h1 class="brand-name">Varnek</h1>
    <p class="contact-phone">555-010-2040</p>
    <p class="contact-web">www.drivevarnek.com</p>
  </section>

  <section class="trailer-side trailer-side--left">
    <svg class="trailer-side__pattern" viewBox="0 0 866 180">
      <polygon role="img" aria-label="Faceted teal triangle pattern at rear end" points="0,0 30,0 122,180 0,180" fill="url(#facet-tones)"/>
      <polygon role="img" aria-label="Faceted teal triangle pattern at front end" points="754,0 866,0 866,180 834,180" fill="url(#facet-tones)"/>
    </svg>
    <div class="brand-mark"></div>
    <h2 class="brand-name">Varnek</h2>
    <p class="contact-phone">555-010-2040</p>
    <p class="contact-web">www.drivevarnek.com</p>
  </section>
</div>
</body>
</html>
```